Thermal Camera flyer

We would like to obtain a sales orientated brochure to promote our two models of thermal imaging cameras as a response to the current Covid 19 health issues. I have provided the text, photos and detailed product specifications , in addition to a sample competitors brochure.
BROCHURE Details : 2 sided - front side to show product, its applications in business, school, hospitals, with text details - Back page to show specifications chart and contact information for QT vista Works. (Melbourne -Sydney-Perth-Brisbane - 1300 847 519
Brochure should be "eye-catching" and reflect the product as a high quality, must-have technology device for todays world.

```html
<!DOCTYPE html>
<html lang="en">
<head>
<meta charset="utf-8">
<title>QT vista Works – Thermal Scanning Camera Flyer</title>
<link rel="stylesheet" href="https://fonts.googleapis.com/css2?family=PT+Sans:wght@400;700&family=PT+Sans+Narrow:wght@400;700&display=swap">
<style>
:root{
  --bg:#e9eaec;
  --blue:#1d5bb6;
  --blue-deep:#123f8a;
  --navy:#1f3f94;
  --ink:#1b1b1b;
  --red:#e8322a;
  --orange:#f08a3a;
  --white:#ffffff;
  --spec-grey:#d4d5d7;
  --black:#0b0d12;
  --thermal:#5fb2ee;
}
*{margin:0;padding:0;box-sizing:border-box}
html,body{width:1200px;height:849px;overflow:hidden}
body{background:var(--bg);font-family:"PT Sans",Arial,sans-serif;position:relative}
.page{position:absolute;top:44px;width:537px;height:760px;overflow:hidden;box-shadow:0 4px 18px rgba(0,0,0,.18)}
.front{left:43px;background:var(--blue)}
.back{left:620px;background:var(--white)}
.abs{position:absolute}

/* brand */
.brand-box{position:absolute;display:flex;align-items:center;gap:14px;padding-left:26px}
.brand-mark{width:22px;height:22px;background:var(--navy)}
.brand-name{font-family:"PT Sans",Arial,sans-serif;font-weight:400;font-size:24px;letter-spacing:.2px}
.front .brand-box{left:112px;top:40px;width:300px;height:58px;border:1px solid var(--white)}
.front .brand-mark{background:var(--blue-deep)}
.front .brand-name{color:var(--white)}
.back .brand-box{left:150px;top:38px;width:310px;height:58px;border:1.5px solid var(--ink)}
.back .brand-name{color:var(--ink)}

/* front */
.dark-band{left:0;top:420px;width:537px;height:340px;background:var(--black)}
.crowd{left:0;top:545px;width:500px;height:215px;background:linear-gradient(180deg,rgba(95,178,238,.2),var(--thermal) 45%,#2f79c9)}
.thermo-bar{left:478px;top:18px;width:16px;height:710px;background:linear-gradient(180deg,#e5242b 0%,var(--orange) 25%,#e8b89a 45%,#9aa3ad 70%,#6d7580 100%)}
.thermo-scale{left:494px;top:18px;width:14px;height:710px;background:repeating-linear-gradient(180deg,rgba(255,255,255,.85) 0 1px,transparent 1px 6px)}
.temp-high{left:400px;top:22px;font-weight:700;font-size:30px;color:transparent;-webkit-text-stroke:1px rgba(255,255,255,.8)}
.temp-normal{left:392px;top:700px;font-weight:700;font-size:30px;color:rgba(255,255,255,.25)}
.eyebrow{left:172px;top:128px;color:var(--orange);font-size:10px;font-weight:700;letter-spacing:1.6px;line-height:1.35;text-transform:uppercase}
.headline{left:172px;top:162px;width:222px;color:var(--white);font-size:17px;font-weight:700;line-height:1.3}
.lede{left:180px;top:282px;width:196px;color:var(--white);font-size:8.4px;line-height:1.4}
.product-floor{left:70px;top:150px;width:80px;height:600px;background:linear-gradient(90deg,#8c939c,#d9dde2 50%,#7a8089);border-radius:6px 6px 2px 2px}
.product-desk{left:402px;top:184px;width:70px;height:320px;background:linear-gradient(180deg,#cfd3d8 0%,#8d949d 60%,#23262c 100%);border-radius:8px}
.tag{position:absolute;border:1px solid rgba(255,255,255,.8);color:var(--white);font-size:7.5px;line-height:1.3;padding:4px 5px}
.tag-floor{left:56px;top:350px;width:56px}
.tag-desk{left:420px;top:300px;width:54px;background:rgba(29,91,182,.85)}
.call{left:212px;top:465px;color:var(--white);font-size:15px;line-height:1.3}
.call strong{color:var(--red);font-weight:700;font-size:16px}

/* back */
.col-main{left:42px;top:112px;width:222px;color:var(--ink);font-size:8.4px;line-height:1.38}
.col-main h2{font-family:"PT Sans Narrow",sans-serif;color:var(--navy);font-size:19px;line-height:1.15;font-weight:700;margin-bottom:9px}
.col-main h2.spaced{margin-top:20px}
.col-main p{margin-bottom:9px}
.spec-box{left:285px;top:130px;width:212px;height:540px;background:var(--spec-grey);border:1.5px solid var(--navy);padding:8px;font-size:6.4px;line-height:1.3;color:var(--ink)}
.spec-box h3{font-size:9.5px;font-weight:700}
.spec-model{font-size:6.4px;margin-bottom:5px}
.spec-box h4{font-size:8px;font-weight:700;margin-top:4px}
.spec-row{display:grid;grid-template-columns:84px 1fr}
.contact{left:0;top:682px;width:537px;text-align:center;color:var(--ink);line-height:1.2}
.contact .company{font-size:12px}
.contact .cities{font-family:"PT Sans Narrow",sans-serif;font-weight:700;font-size:13px;letter-spacing:.4px}
.contact .phone{font-family:"PT Sans Narrow",sans-serif;color:var(--navy);font-weight:700;font-size:22px;line-height:1.15}
.contact .web{font-size:10px;font-weight:700}
</style>
</head>
<body>

<section class="page front">
  <div class="abs dark-band"></div>
  <div class="abs crowd" role="img" aria-label="Thermal imaging view of a crowd of people in blue tones"></div>
  <div class="abs thermo-bar"></div>
  <div class="abs thermo-scale"></div>
  <div class="abs temp-high">40.0°</div>
  <div class="abs temp-normal">36.6°</div>

  <div class="brand-box"><span class="brand-mark"></span><span class="brand-name">QT vista Works</span></div>

  <div class="abs eyebrow">Thermal scanning and<br>facial recognition camera</div>
  <h1 class="abs headline">Identify anyone with a high temperature to detect any potential viruses spreading</h1>
  <p class="abs lede">The temperature of your body is no longer considered private information. That's the stance that businesses around the world are taking as they install thermal imaging cameras for the safety of staff and visitors, often equipped with facial recognition technology, in their buildings in an attempt to cope with the COVID-19 pandemic. It's a movement one might call the automation of temperature checks.</p>

  <div class="abs product-floor" role="img" aria-label="Floor standing thermal camera on a tall silver stand"></div>
  <div class="abs product-desk" role="img" aria-label="Desktop thermal camera on a short stand with triangular base"></div>
  <div class="tag tag-floor">Portable Floor Standing Camera</div>
  <div class="tag tag-desk">Portable Camera for a Reception Desk</div>

  <p class="abs call"><strong>CALL 1300 847 519</strong><br>for further information<br>and a free quote</p>
</section>

<section class="page back">
  <div class="brand-box"><span class="brand-mark"></span><span class="brand-name">QT vista Works</span></div>

  <div class="abs col-main">
    <h2>The Purpose of<br>ThermalScanning<br>&amp; Facial Recognition</h2>
    <p>The purpose is to identify anyone walking into an establishment with a high temperature. This will reduce the likelihood of spreading any potential virus and brings some peace of mind to people in the building.</p>
    <p>We can pair your thermal camera/s with facial recognition software. Employees will check in by standing in front of the camera, which identifies them by their face in just a few seconds without contact (with or without a mask on) and simultaneously performs a thermal scan. It will record a photo of the individual, the date, the time and the temperature reading at that time of entering the building. If the camera detects a high temperature reading, it will sound an alarm in real time and send a notification to a nominated administrator/in-house security.</p>
    <h2 class="spaced">Where and how<br>can it be used?</h2>
    <p>This Camera can be used with access control gates. It is used in office buildings, schools, hotels, hospitality, in fact, any space where Covid is potentially a threat to staff or visitors.</p>
    <p>Our Thermal Scanning &amp; Facial Recognition Camera is used as a safety and security measure. If someone gets sick and takes legal action, you can demonstrate that you have made your best effort to protect your staff and visitors.</p>
  </div>

  <div class="abs spec-box">
    <h3>Technical Specifications</h3>
    <div class="spec-model">Model QV-20 Camera</div>
    <h4>Camera</h4>
    <div class="spec-row"><span>Resolution:</span><span>2 million pixels</span></div>
    <div class="spec-row"><span>Type:</span><span>Binocular wide dynamic camera</span></div>
    <div class="spec-row"><span>Aperture:</span><span>F2.4</span></div>
    <div class="spec-row"><span>Focusing distance:</span><span>50-150cm</span></div>
    <div class="spec-row"><span>White balance:</span><span>auto</span></div>
    <div class="spec-row"><span>Photo flood light</span><span>LED and IR dual photo flood light</span></div>
    <h4>Screen</h4>
    <div class="spec-row"><span>Size:</span><span>8.0 inch IPS LCD screen</span></div>
    <div class="spec-row"><span>Resolution:</span><span>800×1280</span></div>
    <div class="spec-row"><span>Touch:</span><span>Not supported</span></div>
    <h4>Processor</h4>
    <div class="spec-row"><span>CPU:</span><span>QX-40 quad-core</span></div>
    <div class="spec-row"><span>Storage:</span><span>EMMC 8G</span></div>
    <h4>Interface</h4>
    <div class="spec-row"><span>Network module:</span><span>Ethernet and wireless (WIFI)</span></div>
    <div class="spec-row"><span>Audio:</span><span>2.5W / 4R speakers</span></div>
    <div class="spec-row"><span>USB port:</span><span>1 USB OTG, 1 USB HOST standard A</span></div>
    <div class="spec-row"><span>Serial communication:</span><span>1 RS232 serial port</span></div>
    <div class="spec-row"><span>Relay output:</span><span>1 door open signal output</span></div>
    <div class="spec-row"><span>Wiegand One Wiegand:</span><span>26/34 output, one Wiegand 26/34 input</span></div>
    <div class="spec-row"><span>Upgrade button:</span><span>1 RJ45 Ethernet socket</span></div>
    <h4>Function</h4>
    <div class="spec-row"><span>Face Detection:</span><span>Supports facial detection</span></div>
    <div class="spec-row"><span>Face library:</span><span>Up to 30,000</span></div>
    <div class="spec-row"><span>1: N face recognition:</span><span>Support</span></div>
    <div class="spec-row"><span>1: 1 face comparison:</span><span>Support</span></div>
    <div class="spec-row"><span>Stranger detection:</span><span>Support</span></div>
    <div class="spec-row"><span>Identify distance configuration:</span><span>Support</span></div>
    <div class="spec-row"><span>UI interface configuration:</span><span>Support</span></div>
    <div class="spec-row"><span>Upgrade remotely:</span><span>Support</span></div>
    <div class="spec-row"><span>Interface:</span><span>Interfaces include device management, personnel / photo management, record query, etc.</span></div>
    <div class="spec-row"><span>Deployment method:</span><span>Support public cloud deployment, privatized deployment, LAN use, stand-alone use</span></div>
    <h4>Infrared Imaging Thermal Module</h4>
    <div class="spec-row"><span>Temperature detection:</span><span>Support</span></div>
    <div class="spec-row"><span>Temperature detection distance:</span><span>1 meter (optimal distance 0.5 meter)</span></div>
    <div class="spec-row"><span>Temperature:</span><span>≤±0.5 measurement accuracy</span></div>
    <div class="spec-row"><span>Temperature measurement range:</span><span>10–42</span></div>
    <div class="spec-row"><span>Pixels:</span><span>32 X 32 dots (total 1024 pixels)</span></div>
    <div class="spec-row"><span>Visitors' temperature is normal and released directly:</span><span>Support</span></div>
    <div class="spec-row"><span>Abnormal temperature alarm:</span><span>Support (temperature alarm value can be set)</span></div>
  </div>

  <div class="abs contact">
    <div class="company">QT vista Works</div>
    <div class="cities">MELBOURNE – SYDNEY – PERTH – BRISBANE</div>
    <div class="phone">1300 847 519</div>
    <div class="web">www.qtvistaworks.com.au</div>
  </div>
</section>

</body>
</html>
```